massage therapy Business Card Design

massage therapy business card
I would like a custom logo created as well.
My vision is angel wings with the HB business initials in between them.
A very simple design.
Colors preferred are light blues and greens.

Target Market(s)

Massage, Spa, fitness

Industry/Entity Type

Massage Therapy

Contact Information for Business Card

A Harbor Breeze
Nora Campe
Massage Therapist and Veldane Pulse Method Practitioner
2870 Marlow Ridge Road, Conway, AR 72039
501-384-6190
nora.harborbreeze@mailvinto.com

Colors
abd036
33a6d7
3176b5
0255a3
0392cd
9bcb3c
cadf82

Requirements
Must have
• the logo must have angel wing.

```html
<!DOCTYPE html>
<html lang="en">
<head>
<meta charset="UTF-8">
<title>A Harbor Breeze – Business Card</title>
<link rel="stylesheet" href="https://fonts.googleapis.com/css2?family=Montserrat:wght@600;700&display=swap">
<style>
  :root {
    --card-white: #ffffff;
    --brand-green: #9bc42a;
    --band-green: #9cc42b;
    --sky-blue: #0ea0da;
    --deep-blue: #0392cd;
    --text-white: #ffffff;
  }
  html, body {
    margin: 0;
    padding: 0;
    width: 1200px;
    height: 734px;
    overflow: hidden;
    background: var(--card-white);
  }
  .business-card {
    position: relative;
    width: 1200px;
    height: 734px;
    background: var(--card-white);
    font-family: "Montserrat", sans-serif;
  }
  .brand-lockup {
    position: absolute;
    top: 100px;
    left: 0;
    width: 100%;
    text-align: center;
  }
  .brand-name {
    margin: 0;
    font-size: 54px;
    font-weight: 700;
    line-height: 1;
    letter-spacing: 0.01em;
    color: var(--brand-green);
    text-transform: uppercase;
  }
  .owner-name {
    margin: 16px 0 0;
    font-size: 24px;
    font-weight: 700;
    line-height: 1;
    letter-spacing: 0.55em;
    padding-left: 0.55em;
    color: var(--sky-blue);
    text-transform: uppercase;
  }
  .brand-mark {
    position: absolute;
    left: 0;
    top: 250px;
    width: 100%;
    height: 150px;
    display: flex;
    align-items: center;
    justify-content: center;
    gap: 34px;
  }
  .brand-mark-dot {
    width: 130px;
    height: 130px;
    flex: none;
  }
  .brand-mark-initials {
    margin: 0;
    font-size: 132px;
    font-weight: 700;
    line-height: 1;
    letter-spacing: 0.02em;
    color: var(--deep-blue);
  }
  .contact-band {
    position: absolute;
    left: 0;
    bottom: 0;
    width: 100%;
    height: 231px;
    background: var(--band-green);
    display: flex;
    flex-direction: column;
    align-items: center;
    justify-content: center;
    gap: 6px;
    padding-bottom: 24px;
    box-sizing: border-box;
  }
  .contact-line {
    margin: 0;
    font-size: 24px;
    font-weight: 700;
    line-height: 1.25;
    color: var(--text-white);
    text-align: center;
  }
</style>
</head>
<body>
  <div class="business-card">
    <header class="brand-lockup">
      <h1 class="brand-name">A Harbor Breeze</h1>
      <p class="owner-name">Nora Campe</p>
    </header>

    <div class="brand-mark">
      <svg class="brand-mark-dot" viewBox="0 0 130 130" aria-hidden="true">
        <circle cx="65" cy="65" r="65" fill="var(--sky-blue)"/>
      </svg>
      <p class="brand-mark-initials">HB</p>
    </div>

    <footer class="contact-band">
      <p class="contact-line role">Massage Therapist and Veldane Pulse Method Practitioner</p>
      <p class="contact-line address">2870 Marlow Ridge Road, Conway, AR 72039, 501-384-6190</p>
      <p class="contact-line email">nora.harborbreeze@mailvinto.com</p>
    </footer>
  </div>
</body>
</html>
```